250g Condiment Label

Hi, we are looking at re-vamping our 250g label. This is our main label, which covers 70% of our stock. It is overprinted on a thermal printer, it is used for jam, chutney, relish, marmalades etc. We would like to keep it similar so it's recognisable but feel like it could be better.
We require more space to fit the ingredients and a space to print the Best Before date. We do print a barcode on the label so require a space where artwork will not interfere with scanning.
Can the label be reduced to 208mm as it currently overlaps. The width of the band that wraps around the label is currently 4cm. This could go to a maximum of 5 cm. Our preference is to be approx 4.5cm. We would like to keep the security seal tab.
I've attached our current artwork. I'm hoping to see a few options based on this artwork.
Option 1. Please add an additional burgandy band around the base of the label (instead of the black line)
Option 2. More shadowing of the burgundy.
Option 3. Replace stripe background with logo background (as per 300g label sample attached)
Option 4: Your creative input
I would also like to see samples based of our 300g label, see attached. The dimensions need to be the same as the 250g label but lets see what it looks like in black.
1. Handmade Homestyle Quality around border
2. Dots around border
3. Your creative idea.
Please check our website for other labels in our range.
Sauce
Dressings
300g Gourmet https://larderbloom.com.au/gourmet-range/
250g https://larderbloom.com.au/jams/
Mustard & Aioli https://larderbloom.com.au/mustard-aioli-tapenades/
Sauce https://larderbloom.com.au/barbeque-sauce/
Dressings https://larderbloom.com.au/dressings-vinegars/

```html
<!DOCTYPE html>
<html lang="en">
<head>
<meta charset="utf-8">
<title>Hollins Treats – 250g Condiment Label</title>
<link rel="stylesheet" href="https://fonts.googleapis.com/css2?family=Fira+Sans:wght@400;500;600;700&display=swap">
<style>
  :root {
    --charcoal: #333132;
    --gold: #b89a62;
    --gold-light: #d9bf85;
    --cream: #fbe9c3;
    --tab-yellow: #f6e3a0;
    --guide: #22a9d6;
    --ink: #2f2c2b;
  }
  html, body { margin: 0; padding: 0; overflow: hidden; background: #ffffff; }
  .canvas {
    position: relative; width: 1200px; height: 687px; overflow: hidden;
    font-family: "Fira Sans", Arial, sans-serif; color: var(--ink);
  }
  .label-art { position: absolute; inset: 0; }
  .brand-name {
    position: absolute; left: 445px; top: 451px; width: 125px; height: 24px;
    display: flex; align-items: center; justify-content: center; text-align: center;
    font-size: 9.5px; font-weight: 700; letter-spacing: 5px; line-height: 10px;
    color: var(--charcoal); padding-left: 5px; box-sizing: border-box;
  }
  .maker-info {
    position: absolute; left: 111px; top: 463px; width: 140px; text-align: center;
    font-size: 9.2px; line-height: 10px;
  }
  .maker-info p { margin: 0; }
  .maker-info .heading { font-weight: 600; }
  .maker-info .address { margin: 5px 0 6px; }
  .maker-info .allergen { font-size: 7.4px; line-height: 8.2px; margin-top: 4px; }
  .nutrition {
    position: absolute; left: 805px; top: 467px; width: 152px;
    font-size: 9px; line-height: 9.2px;
  }
  .nutrition p { margin: 0; }
  .nutrition .title { font-weight: 600; }
  .nutrition .columns { text-align: right; margin: 2.8px 3px 3.8px 0; }
  .nutrition ul { list-style: none; margin: 0; padding: 0; }
  .tagline {
    position: absolute; left: 490px; top: 601px; width: 146px; text-align: center;
    font-size: 8.6px; line-height: 12px; font-weight: 600; color: var(--gold); letter-spacing: 0.3px;
  }
</style>
</head>
<body>
<div class="canvas">
  <svg class="label-art" width="1200" height="687" viewBox="0 0 1200 687" xmlns="http://www.w3.org/2000/svg">
    <defs>
      <pattern id="dot-row" x="97" y="0" width="11.8" height="687" patternUnits="userSpaceOnUse">
        <circle cx="5.9" cy="437" r="2.1" fill="var(--gold)"/>
        <circle cx="5.9" cy="607" r="2.1" fill="var(--gold)"/>
      </pattern>
      <pattern id="dot-col" x="0" y="187" width="687" height="11.8" patternUnits="userSpaceOnUse">
        <circle cx="487" cy="5.9" r="2.1" fill="var(--gold)"/>
        <circle cx="529" cy="5.9" r="2.1" fill="var(--gold)"/>
      </pattern>
      <linearGradient id="emblem-tone" x1="0" y1="0" x2="1" y2="1">
        <stop offset="0" stop-color="#e2c68d"/>
        <stop offset="0.55" stop-color="#b89a62"/>
        <stop offset="1" stop-color="#8a6f3f"/>
      </linearGradient>
    </defs>

    <!-- security seal tab -->
    <rect class="seal-stem" x="470" y="180" width="76" height="240" fill="var(--charcoal)"/>
    <polygon class="seal-top" points="508,58 590,140 508,222 426,140" fill="var(--charcoal)"/>
    <rect class="seal-strip" x="494" y="189" width="29" height="190" fill="var(--cream)"/>
    <rect class="seal-dots" x="480" y="187" width="56" height="190" fill="url(#dot-col)"/>

    <!-- wrap band -->
    <rect class="band" x="96" y="415" width="923" height="215" fill="var(--charcoal)"/>
    <rect class="glue-tab" x="1019" y="415" width="87" height="215" fill="var(--tab-yellow)"/>
    <rect class="band-panel" x="96" y="448" width="923" height="143" fill="var(--cream)"/>
    <rect class="band-rule" x="96" y="443" width="923" height="5" fill="var(--gold)"/>
    <rect class="band-rule" x="96" y="591" width="923" height="6" fill="var(--gold)"/>
    <rect class="band-dots" x="97" y="432" width="342" height="10" fill="url(#dot-row)"/>
    <rect class="band-dots" x="576" y="432" width="442" height="10" fill="url(#dot-row)"/>
    <rect class="band-dots" x="97" y="602" width="390" height="10" fill="url(#dot-row)"/>
    <rect class="band-dots" x="635" y="602" width="383" height="10" fill="url(#dot-row)"/>

    <!-- centre badge mount: flared stem, diamond and name plate -->
    <polygon class="badge-flare" points="470,375 431,415 585,415 546,375" fill="var(--charcoal)"/>
    <polygon class="badge-mount" points="508,358 580,430 508,502 436,430" fill="var(--charcoal)"/>
    <rect class="name-plate-mount" x="436" y="443" width="143" height="41" fill="var(--charcoal)"/>

    <!-- emblem artwork areas -->
    <polygon role="img" aria-label="Gold emblem illustration area" points="508,90 559,140 508,190 457,140" fill="url(#emblem-tone)"/>
    <polygon role="img" aria-label="Gold emblem illustration area" points="507,373 563,429 507,485 451,429" fill="url(#emblem-tone)"/>
    <rect class="name-plate-mount" x="436" y="445" width="143" height="39" fill="var(--charcoal)"/>
    <polygon points="491,484 507,485 523,484 507,478" fill="url(#emblem-tone)"/>
    <rect class="name-plate" x="445" y="451" width="125" height="24" fill="var(--gold-light)"/>

    <!-- cutter guides -->
    <g fill="none" stroke="var(--guide)" stroke-width="0.5">
      <polyline points="484,380 484,178 446,140 508,78 570,140 532,178 532,380"/>
      <polyline points="437,429 110,429 110,616 1094,616 1094,429 579,429"/>
    </g>

    <!-- nutrition rules -->
    <g stroke="var(--ink)">
      <line x1="802" y1="497" x2="958" y2="497" stroke-width="1"/>
      <line x1="802" y1="508" x2="958" y2="508" stroke-width="0.8"/>
      <line x1="802" y1="577" x2="958" y2="577" stroke-width="1"/>
    </g>

    <!-- origin badge placeholder -->
    <rect class="origin-badge" x="971" y="458" width="40" height="129" rx="3" fill="none" stroke="var(--ink)" stroke-width="1.4"/>
  </svg>

  <div class="brand-name">HOLLINS<br>TREATS</div>

  <div class="maker-info">
    <p class="heading">Proudly Australian<br>owned and made</p>
    <p class="address">Larder Bloom<br>14 Mill Paddock Road<br>Wattle Grove 2599<br>Ph (02) 5550 1234<br>www.larderbloom.com.au</p>
    <p class="heading">HACCP Accredited</p>
    <p class="allergen">Made on a production line that<br>also produces products containing<br>eggs, nuts, dairy and soy.</p>
  </div>

  <div class="nutrition">
    <p class="title">Nutritional Information<br>Serving size<br>Serves per pack</p>
    <p class="columns">Per Serve&nbsp; Per 100g</p>
    <ul>
      <li>Energy</li><li>Protein</li><li>Fat, total</li><li>–Saturated</li>
      <li>Carbohydrate</li><li>–Sugar</li><li>Sodium</li>
    </ul>
  </div>

  <div class="tagline">Handmade Homestyle Quality</div>
</div>
</body>
</html>
```